Bref créative
business cards and stationary set
vAmu Business cards and stationary
Bright & Fun-filled
Petra Veselinek
Marketing Manager
4127 Marlow Crest Pkwy,
Suite 240
Irving, TX, 75418
petra@vamuleaf.com
www.vamuleaf.com
Logo
picture
picture 2

```html
<!DOCTYPE html>
<html lang="en">
<head>
<meta charset="utf-8">
<title>vAmu Stationery Set</title>
<link href="https://fonts.googleapis.com/css2?family=Montserrat:wght@400;600;700&display=swap" rel="stylesheet">
<style>
:root{
  --bg-top:#4a4a4a;
  --bg-bottom:#2b2b2b;
  --ink:#111111;
  --paper:#ffffff;
  --green:#39e01c;
  --green-dark:#22b30c;
  --ghost:#ececec;
  --caption:#9a9a9a;
  --muted:#bdbdbd;
}
*{margin:0;padding:0;box-sizing:border-box}
html,body{width:1200px;height:346px;overflow:hidden}
body{
  position:relative;
  font-family:"Montserrat",Arial,sans-serif;
  background:radial-gradient(ellipse at 50% 40%,var(--bg-top),var(--bg-bottom));
}
.piece{position:absolute;overflow:hidden;box-shadow:0 3px 8px rgba(0,0,0,.45)}
.caption{position:absolute;font-size:5px;color:var(--caption);text-align:center;letter-spacing:.3px}
.wordmark{font-weight:700;color:var(--paper);letter-spacing:.5px;display:flex;align-items:center;gap:3px}
.wordmark .dot{width:.7em;height:.7em;border-radius:50%;background:var(--green)}
.wordmark.dark{color:var(--ink)}

/* brand block */
.brand{position:absolute;left:22px;top:58px}
.brand .wordmark{font-size:30px}
.brand .tagline{font-size:6px;color:var(--muted);margin-top:3px;letter-spacing:.6px}

/* business cards */
.card-back{left:22px;top:172px;width:80px;height:48px;background:var(--ink)}
.card-back .band{position:absolute;left:0;bottom:0;width:100%;height:12px;background:var(--green)}
.card-front{left:12px;top:168px;width:84px;height:50px;background:var(--ink)}
.card-front .wordmark{position:absolute;left:6px;top:6px;font-size:9px}
.card-front .details{position:absolute;left:6px;top:20px;font-size:3.2px;line-height:4.3px;color:var(--paper)}
.card-front .details b{color:var(--green);font-weight:600}
.card-front svg{position:absolute;left:0;bottom:0}

/* letterheads */
.letterhead{top:19px;width:228px;height:305px;background:var(--paper)}
.letterhead.one{left:163px}
.letterhead.two{left:403px}
.letterhead .header{position:absolute;left:0;top:0;width:100%;height:34px;background:var(--ink)}
.letterhead .header .wordmark{position:absolute;left:50%;transform:translateX(-50%);top:9px;font-size:11px}
.letterhead .header .contact{position:absolute;right:14px;top:8px;font-size:3px;line-height:4px;color:var(--paper);text-align:right}
.letterhead .ghost{position:absolute;left:0;top:130px;width:100%;text-align:center;font-size:52px;font-weight:700;color:var(--ghost)}
.letterhead svg{position:absolute;left:0;bottom:0}

/* compliment slips */
.slip{left:643px;width:221px;background:var(--paper)}
.slip.top{top:67px;height:101px}
.slip.bottom{top:209px;height:108px}
.slip .header{position:absolute;left:0;top:0;width:100%;height:26px;background:var(--ink)}
.slip .header .wordmark{position:absolute;left:50%;transform:translateX(-50%);top:7px;font-size:9px}
.slip .header .contact{position:absolute;right:10px;top:6px;font-size:3px;line-height:4px;color:var(--paper);text-align:right}
.slip svg{position:absolute;left:0;bottom:0}

/* envelopes */
.envelope{left:883px;width:293px;background:var(--paper)}
.envelope.front{top:62px;height:106px}
.envelope.back{top:202px;height:117px}
.envelope.front .wordmark{position:absolute;left:14px;top:10px;font-size:10px}
.envelope.front .address{position:absolute;left:14px;top:26px;font-size:3.2px;line-height:4.3px;color:var(--ink)}
.envelope svg{position:absolute;left:0;top:0}
.envelope.back .wordmark{position:absolute;left:50%;transform:translateX(-50%);top:14px;font-size:9px;z-index:2}
</style>
</head>
<body>

<div class="brand">
  <div class="wordmark"><span class="dot"></span>vAmu</div>
  <div class="tagline">Business Stationery</div>
</div>

<div class="piece card-back"><div class="band"></div></div>
<div class="piece card-front">
  <div class="wordmark"><span class="dot"></span>vAmu</div>
  <div class="details">
    <b>Petra Veselinek</b><br>Marketing Manager<br>4127 Marlow Crest Pkwy, Suite 240<br>Irving, TX, 75418<br>petra@vamuleaf.com<br>www.vamuleaf.com
  </div>
  <svg width="84" height="10" viewBox="0 0 84 10"><path d="M0 10 L0 4 Q42 -2 84 6 L84 10 Z" fill="var(--green)"/></svg>
</div>
<div class="caption" style="left:12px;top:226px;width:90px">Business card</div>

<div class="piece letterhead one">
  <div class="header">
    <div class="wordmark"><span class="dot"></span>vAmu</div>
    <div class="contact">4127 Marlow Crest Pkwy<br>Suite 240, Irving, TX, 75418<br>petra@vamuleaf.com<br>www.vamuleaf.com</div>
  </div>
  <div class="ghost">vAmu</div>
  <svg width="228" height="22" viewBox="0 0 228 22"><path d="M0 22 L0 8 Q114 -4 228 10 L228 22 Z" fill="var(--green)"/><path d="M0 22 L0 16 Q114 6 228 18 L228 22 Z" fill="var(--green-dark)"/></svg>
</div>
<div class="caption" style="left:163px;top:328px;width:228px">Letterhead</div>

<div class="piece letterhead two">
  <div class="ghost">vAmu</div>
  <svg width="228" height="22" viewBox="0 0 228 22"><path d="M0 22 L0 8 Q114 -4 228 10 L228 22 Z" fill="var(--green)"/><path d="M0 22 L0 16 Q114 6 228 18 L228 22 Z" fill="var(--green-dark)"/></svg>
</div>
<div class="caption" style="left:403px;top:328px;width:228px">Letterhead</div>

<div class="piece slip top">
  <div class="header">
    <div class="wordmark"><span class="dot"></span>vAmu</div>
    <div class="contact">4127 Marlow Crest Pkwy<br>Suite 240, Irving, TX, 75418<br>www.vamuleaf.com</div>
  </div>
</div>
<div class="caption" style="left:643px;top:172px;width:221px">Compliment slip</div>

<div class="piece slip bottom">
  <div class="header">
    <div class="wordmark"><span class="dot"></span>vAmu</div>
    <div class="contact">petra@vamuleaf.com<br>www.vamuleaf.com</div>
  </div>
  <svg width="221" height="16" viewBox="0 0 221 16"><path d="M0 16 L0 6 Q110 -3 221 8 L221 16 Z" fill="var(--green)"/></svg>
</div>
<div class="caption" style="left:643px;top:321px;width:221px">Compliment slip</div>

<div class="piece envelope front">
  <svg width="293" height="106" viewBox="0 0 293 106">
    <path d="M0 0 L293 0 L293 20 Q146 60 0 14 Z" fill="var(--green)"/>
    <path d="M0 106 L0 92 Q146 70 293 96 L293 106 Z" fill="var(--green)"/>
  </svg>
  <div class="wordmark dark" style="z-index:2"><span class="dot"></span>vAmu</div>
  <div class="address">4127 Marlow Crest Pkwy, Suite 240<br>Irving, TX, 75418</div>
</div>
<div class="caption" style="left:883px;top:172px;width:293px">DL envelope</div>

<div class="piece envelope back">
  <svg width="293" height="117" viewBox="0 0 293 117">
    <path d="M0 117 L146 55 L293 117 Z" fill="#f4f4f4"/>
    <path d="M0 0 L293 0 L293 8 Q146 80 0 8 Z" fill="var(--green)"/>
    <path d="M0 0 L293 0 L293 4 Q146 64 0 4 Z" fill="var(--ink)"/>
  </svg>
  <div class="wordmark"><span class="dot"></span>vAmu</div>
</div>
<div class="caption" style="left:883px;top:323px;width:293px">DL envelope</div>

</body>
</html>
```